Newsletter Banner for email based newsletter

Newsletter banner with Veltrix as the main focus and our other 2 companies Morrow and Clearance Partners, included. 72 dpi and in RGB color mode, the banner should be the same dimensions as the attached example (VeltrixNewsHeader2). I have also attached the Veltrix and other logos. Note as soon as we receive a decent banner we will accept it as the period for this is only 1 day.

```html
<!DOCTYPE html>
<html lang="en">
<head>
<meta charset="utf-8">
<title>Veltrix Newsletter Banner</title>
<link rel="stylesheet" href="https://fonts.googleapis.com/css2?family=Montserrat:wght@300;800&family=Oswald:wght@700&display=swap">
<style>
  :root {
    --brand-blue: #1f5a99;
    --brand-gray: #6d6e71;
    --orange: #f47b20;
    --orange-light: #f8a967;
    --white: #ffffff;
    --lab-light: #eef3fb;
    --lab-mid: #b9c9e6;
    --lab-deep: #5f7fb8;
  }
  html, body { margin: 0; padding: 0; overflow: hidden; background: var(--white); }
  .banner {
    position: relative;
    width: 1200px;
    height: 214px;
    overflow: hidden;
    background: var(--white);
    font-family: "Montserrat", Arial, sans-serif;
  }
  .brand {
    position: absolute;
    left: 24px;
    top: 34px;
    display: flex;
    align-items: center;
    gap: 12px;
  }
  .brand-mark {
    width: 40px;
    height: 40px;
    background: var(--brand-blue);
  }
  .brand-name {
    margin: 0;
    font-weight: 800;
    font-size: 44px;
    line-height: 1;
    letter-spacing: 1px;
    color: var(--brand-blue);
    text-transform: uppercase;
  }
  .brand-sub {
    position: absolute;
    left: 178px;
    top: 86px;
    font-size: 15px;
    font-weight: 300;
    color: var(--brand-blue);
  }
  .sister {
    position: absolute;
    top: 118px;
    margin: 0;
    font-weight: 300;
    font-size: 22px;
    line-height: 22px;
  }
  .sister--clearance { left: 24px; color: var(--brand-gray); }
  .sister--morrow { left: 172px; color: var(--brand-blue); }
  .lab-photo {
    position: absolute;
    left: 318px;
    top: 0;
    width: 712px;
    height: 214px;
    background:
      radial-gradient(ellipse 120px 110px at 520px 55px, var(--white) 0%, rgba(255,255,255,0) 100%),
      radial-gradient(ellipse 90px 70px at 640px 175px, var(--lab-light) 0%, rgba(238,243,251,0) 100%),
      linear-gradient(90deg, var(--white) 0%, var(--lab-light) 18%, var(--lab-mid) 45%, var(--lab-deep) 70%, var(--lab-mid) 100%);
  }
  .issue-panel {
    position: absolute;
    left: 1029px;
    top: 0;
    width: 171px;
    height: 214px;
  }
  .issue-panel svg { display: block; }
  .issue-label {
    position: absolute;
    left: 0;
    top: 88px;
    width: 171px;
    margin: 0;
    text-align: center;
    font-family: "Oswald", "Arial Narrow", sans-serif;
    font-weight: 700;
    font-size: 26px;
    letter-spacing: 0.5px;
    color: var(--white);
  }
</style>
</head>
<body>
  <header class="banner">
    <div class="brand">
      <div class="brand-mark"></div>
      <h1 class="brand-name">Veltrix</h1>
    </div>
    <div class="brand-sub">Laboratories</div>
    <p class="sister sister--clearance">clearance<br>partners</p>
    <p class="sister sister--morrow">morrow<br>laboratories</p>

    <div class="lab-photo" role="img" aria-label="Laboratory photograph with a microscope and glass flasks in soft blue light"></div>

    <div class="issue-panel">
      <svg width="171" height="214" viewBox="0 0 171 214" aria-hidden="true">
        <rect width="171" height="214" fill="var(--orange-light)"/>
        <path d="M0 0 H171 V118 C120 150 60 150 0 160 Z" fill="var(--orange)"/>
      </svg>
      <p class="issue-label">NEWSLETTER</p>
    </div>
  </header>
</body>
</html>
```